Pelvoro Mobile App

I need a professional, sleek design for a new mobile application for iPhone. The application will be the mobile counterpart to the current website (www.pelvoro-example.com - please refer to site for existing web design).
Pelvoro is a photo social network which focuses on content aggregation, search and real-time photo discovery.
I need a clean, modern, minimalistic design for the mobile app which will run on iPhone, including minimalistic page and button designs.
I've attached undesigned screenshots of the current application build to give an idea of the functionality and pages available within the application.
The app will have the following pages/functionality:
- photo feed of other users' images; data presented: photo, photo caption, user name, date
- upload photo
- save photo
- photo search; available search criteria: keywords, dates (from/to), location
Target Market(s)
Photographers/Photo enthusiasts, bloggers, social networking
Industry/Entity Type
Build
Look and feel
Each slider illustrates characteristics of the customer's brand and the style your logo design should communicate.

```html
<!DOCTYPE html>
<html lang="en">
<head>
<meta charset="utf-8">
<title>Pelvoro — Home</title>
<link rel="stylesheet" href="https://fonts.googleapis.com/css2?family=Ubuntu:ital,wght@0,400;0,500;0,700;1,400&display=swap">
<style>
  :root {
    --bg-dark: #232427;
    --bg-mid: #34363a;
    --card: #16171a;
    --card-edge: #2c2d31;
    --header: #050505;
    --text: #f2f2f2;
    --muted: #8b8d92;
    --green: #7ab32e;
    --green-dark: #4f7d1a;
    --blue: #3ab4f2;
    --icon: #b9bcc0;
    --tab: #1c1d20;
  }
  * { box-sizing: border-box; margin: 0; padding: 0; }
  html, body { width: 676px; height: 1200px; overflow: hidden; }
  body {
    position: relative;
    font-family: "Ubuntu", sans-serif;
    background: linear-gradient(90deg, var(--bg-dark) 0%, var(--bg-mid) 8%, var(--bg-mid) 92%, var(--bg-dark) 100%);
    color: var(--text);
  }

  /* Header */
  .app-header {
    position: absolute; top: 0; left: 0; width: 676px; height: 101px;
    background: linear-gradient(180deg, #1a1a1a 0%, var(--header) 50%, #000 100%);
    z-index: 5;
    box-shadow: 0 2px 6px rgba(0,0,0,.6);
  }
  .sign-out {
    position: absolute; left: 21px; top: 32px; width: 151px; height: 37px;
    background: linear-gradient(180deg, #8cc63f, var(--green-dark));
    clip-path: polygon(14px 0, 100% 0, 100% 100%, 14px 100%, 0 50%);
    border-radius: 3px;
    color: #fff; font-size: 18px; font-weight: 500;
    display: flex; align-items: center; padding-left: 28px; gap: 18px;
  }
  .app-title {
    position: absolute; left: 0; right: 0; top: 30px; text-align: center;
    font-size: 31px; font-weight: 700; letter-spacing: 1px; color: #fff;
  }
  .search-field {
    position: absolute; left: 496px; top: 19px; width: 151px; height: 63px;
    background: #fff; border: 3px solid #c9ccd1; border-radius: 32px;
    color: #b6b9bd; font-size: 26px; display: flex; align-items: center; justify-content: center;
  }

  /* Feed cards */
  .photo-card {
    position: absolute; left: 57px; width: 561px;
    background: var(--card); border-radius: 6px;
    border: 1px solid var(--card-edge);
    box-shadow: 0 3px 8px rgba(0,0,0,.45);
  }
  .photo {
    position: absolute; left: 10px; right: 10px;
  }
  .photo-caption { position: absolute; left: 10px; }
  .photo-title { font-size: 27px; font-weight: 400; color: var(--text); }
  .photo-author { font-size: 15px; font-style: italic; color: var(--muted); margin-top: 1px; }
  .photo-actions { position: absolute; right: 30px; display: flex; align-items: center; gap: 14px; }

  /* Loading */
  .loading-toast {
    position: absolute; left: 237px; top: 533px; width: 200px; height: 121px;
    background: rgba(20,21,23,.97); border-radius: 8px; z-index: 4;
    box-shadow: 0 2px 10px rgba(0,0,0,.5);
    display: flex; flex-direction: column; align-items: center; padding-top: 24px;
  }
  .loading-label { font-size: 15px; font-style: italic; color: #9a9ca0; margin-top: 10px; }

  /* Tab bar */
  .tab-bar {
    position: absolute; left: 0; top: 1101px; width: 676px; height: 99px;
    background: linear-gradient(180deg, #2b2c30 0%, #141518 55%, #0b0c0d 100%);
    border-top: 1px solid #3a3b3f; z-index: 5;
    display: flex; align-items: center;
  }
  .tab { width: 161px; height: 92px; display: flex; align-items: center; justify-content: center; }
  .tab:first-child { width: 175px; }
  .tab.is-active { background: linear-gradient(180deg, #3a3b3f, #26272a); border-radius: 3px; }
</style>
</head>
<body>

<header class="app-header">
  <div class="sign-out">
    <svg width="10" height="16" viewBox="0 0 10 16"><path d="M8 2 L2 8 L8 14" fill="none" stroke="#2f4d0f" stroke-width="3"/></svg>
    <span>Sign Out</span>
  </div>
  <h1 class="app-title">HOME</h1>
  <div class="search-field">Search</div>
</header>

<article class="photo-card" style="top:80px; height:462px;">
  <div class="photo" role="img" aria-label="Photo of a hilltop fort above a city at twilight" style="top:21px; height:355px; background: linear-gradient(180deg, #4d3b4a 0%, #a4534a 30%, #6f4a45 52%, #5a4a3a 68%, #3b3128 100%);"></div>
  <div class="photo-caption" style="top:388px;">
    <div class="photo-title">Fort Grey Twilight</div>
    <div class="photo-author">by User McUser</div>
  </div>
  <div class="photo-actions" style="top:394px;">
    <svg width="36" height="28" viewBox="0 0 36 28"><path d="M3 12 h9 l3 5 h6 l3 -5 h9 v13 H3 Z" fill="none" stroke="#e6e6e6" stroke-width="3"/><path d="M18 1 v11 M13 7 l5 5 5 -5" stroke="#e6e6e6" stroke-width="3" fill="none"/></svg>
    <svg width="42" height="36" viewBox="0 0 42 36"><path d="M21 35 C8 25 1 18 1 10 A9.5 9.5 0 0 1 21 6 A9.5 9.5 0 0 1 41 10 C41 18 34 25 21 35 Z" fill="#7ab32e"/></svg>
  </div>
</article>

<div class="loading-toast">
  <svg width="48" height="48" viewBox="-24 -24 48 48">
    <g stroke-width="3.5" stroke-linecap="round">
      <line x1="0" y1="-20" x2="0" y2="-11" stroke="#555" transform="rotate(0)"/>
      <line x1="0" y1="-20" x2="0" y2="-11" stroke="#666" transform="rotate(30)"/>
      <line x1="0" y1="-20" x2="0" y2="-11" stroke="#777" transform="rotate(60)"/>
      <line x1="0" y1="-20" x2="0" y2="-11" stroke="#888" transform="rotate(90)"/>
      <line x1="0" y1="-20" x2="0" y2="-11" stroke="#999" transform="rotate(120)"/>
      <line x1="0" y1="-20" x2="0" y2="-11" stroke="#aaa" transform="rotate(150)"/>
      <line x1="0" y1="-20" x2="0" y2="-11" stroke="#bbb" transform="rotate(180)"/>
      <line x1="0" y1="-20" x2="0" y2="-11" stroke="#ccc" transform="rotate(210)"/>
      <line x1="0" y1="-20" x2="0" y2="-11" stroke="#ddd" transform="rotate(240)"/>
      <line x1="0" y1="-20" x2="0" y2="-11" stroke="#444" transform="rotate(270)"/>
      <line x1="0" y1="-20" x2="0" y2="-11" stroke="#444" transform="rotate(300)"/>
      <line x1="0" y1="-20" x2="0" y2="-11" stroke="#4a4a4a" transform="rotate(330)"/>
    </g>
  </svg>
  <div class="loading-label">Loading</div>
</div>

<article class="photo-card" style="top:557px; height:457px;">
  <div class="photo" role="img" aria-label="Photo of an umbrella reflected in a rain puddle" style="top:10px; height:361px; background: linear-gradient(135deg, #3f9a8a 0%, #8d7c5a 30%, #d8c990 55%, #b9a773 75%, #4f6a6a 100%);"></div>
  <div class="photo-caption" style="top:378px;">
    <div class="photo-title">After Rain Happiness</div>
    <div class="photo-author">by User McUser</div>
  </div>
  <div class="photo-actions" style="top:384px;">
    <svg width="36" height="28" viewBox="0 0 36 28"><path d="M3 12 h9 l3 5 h6 l3 -5 h9 v13 H3 Z" fill="none" stroke="#e6e6e6" stroke-width="3"/><path d="M18 1 v11 M13 7 l5 5 5 -5" stroke="#e6e6e6" stroke-width="3" fill="none"/></svg>
    <svg width="42" height="36" viewBox="0 0 42 36"><path d="M21 35 C8 25 1 18 1 10 A9.5 9.5 0 0 1 21 6 A9.5 9.5 0 0 1 41 10 C41 18 34 25 21 35 Z" fill="#f2f2f2"/></svg>
  </div>
</article>

<article class="photo-card" style="top:1032px; height:120px;">
  <div class="photo" role="img" aria-label="Photo of a glass bottle against colourful bokeh lights" style="top:10px; height:110px; background: linear-gradient(90deg, #2b3f8a 0%, #c0503a 30%, #d89a3a 55%, #6a5aa8 80%, #2a6fb0 100%);"></div>
</article>

<nav class="tab-bar">
  <div class="tab">
    <svg width="70" height="48" viewBox="0 0 70 48"><g fill="none" stroke="#a7aaae" stroke-width="7"><path d="M2 12 h14 c12 0 18 24 30 24 h10"/><path d="M2 36 h14 c12 0 18 -24 30 -24 h10"/></g><path d="M54 2 l14 10 -14 10 Z M54 26 l14 10 -14 10 Z" fill="#a7aaae"/></svg>
  </div>
  <div class="tab is-active">
    <svg width="60" height="56" viewBox="0 0 60 56"><g fill="#3ab4f2"><path d="M30 2 L58 16 H2 Z"/><rect x="4" y="18" width="52" height="4"/><rect x="9" y="24" width="8" height="22"/><rect x="26" y="24" width="8" height="22"/><rect x="43" y="24" width="8" height="22"/><rect x="2" y="48" width="56" height="6"/></g></svg>
  </div>
  <div class="tab">
    <svg width="72" height="56" viewBox="0 0 72 56"><path d="M4 14 h18 l6 -10 h16 l6 10 h18 v40 H4 Z" fill="#a7aaae"/><circle cx="36" cy="33" r="15" fill="#2b2c30"/><path d="M36 24 v18 M29 31 l7 -7 7 7" stroke="#a7aaae" stroke-width="4" fill="none"/></svg>
  </div>
  <div class="tab">
    <svg width="70" height="50" viewBox="0 0 70 50"><rect x="2" y="4" width="66" height="44" rx="4" fill="#a7aaae"/><rect x="8" y="10" width="22" height="30" fill="#2b2c30"/><circle cx="19" cy="20" r="5" fill="#a7aaae"/><path d="M11 36 a8 8 0 0 1 16 0 Z" fill="#a7aaae"/><g fill="#2b2c30"><rect x="35" y="13" width="26" height="3"/><rect x="35" y="21" width="26" height="3"/><rect x="35" y="29" width="26" height="3"/><rect x="35" y="37" width="26" height="3"/></g></svg>
  </div>
</nav>

</body>
</html>
```